Pamphlet Days of the Family - École Sainte-Ondine

We * need a pamphlet (flyer) to describe a new project. This project is called "Family Days - École Sainte-Ondine". The text describing family days and their intended goals is attached in the downloaded .doc document. We also provided the logo (LA PRIMOVEL no font in attachment) which represents the school and those days of the family. Please write "Family Days - École Sainte-Ondine" on top of the pamphlet with the Logo in plain view (The text The days of the École Sainte-Ondine family must be associated with the logo). We need the pamphlet to be colorful, attractive and clean as much as possible. We would like to have childish drawings (see drawing example attached) and photos that represent one or both parents with their child (ren) in a SCHOOL ENVIRONMENT (very important). Parents must feel concerned. It can be a two-sided pamphlet. In color (bright colors as much as possible). The text must be in French so only FRENCH DESIGNERS ARE INVITED to work on this design because the text must remain consistent. The project can be summed up as follows: The Sainte-Ondine School wishes to open its doors so that parents can share with their child moments in their student life. They will be invited, at various times of the school year, to participate in the daily life of their child, for example ... • during special activities in class (eg reading, do-it-yourself, job presentation, etc.). events (eg, back to school, Christmas choir, carnival, etc.) • during educational and sports outings (eg skating, library, cinema, etc.) Also, they will have the opportunity to come and spend a period in their child's classroom. They will have the privilege of accompanying him during a usual learning moment. For any additional question, thank you to contact me via this page, it will be my pleasure to answer you quickly. Thank you all for your participation. * We are a committee made up of parents, teachers, school principal, school administrators. Everyone has a say in the final design. So I am only the intermediary responsible for the project. It will be my pleasure to share with you the information received from these different partners for this project.

Target Market(s)

Parents of students at a primary school (ages 5 to 12).

Font styles to use
Sans Serif

Colors

Designer to choose colors to be used in the design.

Requirements
Must have
• The Logo prominently Pamphlet Colorful (beautiful bright colors) Easy to read and understand (some parents speak very little French) Originality (Attractive) Text In French (required) and consistent
Nice to have
• One or more Childish Drawing (s) One (1) parent-child Photo (s) in a school environment Allure Épuré
Should not have
• The Dark Colors Of the Scriptures Too Small A Condensed Text Text English

```html
<!DOCTYPE html>
<html lang="fr">
<head>
<meta charset="utf-8">
<title>Les journées de la famille – École Sainte-Ondine</title>
<link href="https://fonts.googleapis.com/css2?family=Exo+2:wght@600;700&family=Lato:ital,wght@0,400;0,700;1,400&display=swap" rel="stylesheet">
<style>
  :root{
    --backdrop:#4a555d;
    --paper:#ffffff;
    --ink:#1f1f1f;
    --title-red:#e0393a;
    --title-green:#9bc31c;
    --sky-light:#e4f4fb;
    --sky:#a9dcf2;
    --grass:#a6d84a;
    --grass-dark:#6fb62a;
    --note-fill:#fdec9e;
    --note-line:#ec5a4a;
    --circle-fill:#c7e66a;
    --circle-line:#e64a3b;
    --bullet:#3ea23a;
    --arrow:#d8393a;
    --logo-sun:#f7d21c;
  }
  *{box-sizing:border-box;margin:0;padding:0}
  html,body{width:1200px;height:1200px;overflow:hidden}
  body{background:var(--backdrop);font-family:"Lato",sans-serif;color:var(--ink);position:relative}
  .flyer{position:absolute;left:158px;top:28px;width:884px;height:1144px;background:var(--paper);overflow:hidden}
  .header{position:absolute;left:0;top:0;width:884px;height:419px;
    background:linear-gradient(180deg,var(--sky-light) 0%,var(--sky) 55%,var(--sky-light) 88%,var(--grass) 91%,var(--grass-dark) 100%)}
  .header-illustration{position:absolute;left:410px;top:20px;width:451px;height:357px;border-radius:40px;
    background:radial-gradient(ellipse at 40% 35%,#c9ec8a 0%,#a9dcf2 60%,rgba(169,220,242,0) 75%)}
  .brand{position:absolute;left:150px;top:70px;width:160px;height:100px;display:flex;align-items:center;gap:8px}
  .brand-dot{width:34px;height:34px;border-radius:50%;background:var(--logo-sun);flex:none}
  .brand-name{font-family:"Lato",sans-serif;font-weight:700;font-size:18px;color:#e8a712;letter-spacing:.5px}
  .title{position:absolute;left:48px;top:222px;font-family:"Exo 2",sans-serif;line-height:1.1}
  .title-line1{font-size:32px;font-weight:600;color:var(--title-red);display:block}
  .title-line2{font-size:40px;font-weight:700;color:var(--title-green);display:block}
  .body{position:absolute;left:38px;top:443px;width:807px;font-size:12.4px;line-height:1.25}
  .body p{text-align:justify;margin-bottom:11px}
  .checks{display:grid;grid-template-columns:1fr 1fr;column-gap:60px;row-gap:4px;list-style:none;margin:-6px 0 11px 6px}
  .checks li{display:flex;gap:10px;align-items:flex-start}
  .checks svg{flex:none;margin-top:2px}
  .checks .right{grid-column:2;grid-row:1}
  .note{position:absolute;background:var(--note-fill);border:1.5px solid var(--note-line);border-radius:8px;padding:4px 8px;font-size:12.4px;line-height:1.25}
  .note h3{font-size:13.5px;font-weight:700;text-align:center;margin-bottom:3px}
  .note ul{list-style:none}
  .note li{position:relative;padding-left:16px;margin-bottom:4px}
  .note li::before{content:"";position:absolute;left:2px;top:6px;width:5px;height:5px;border-radius:50%;background:var(--bullet)}
  .role{position:absolute;width:84px;height:84px;border-radius:50%;background:var(--circle-fill);border:2px solid var(--circle-line);
    display:flex;align-items:center;justify-content:center;text-align:center;font-weight:700;font-size:12.5px;line-height:1.6}
  .role.small{font-size:11px}
  .hub{position:absolute;left:354px;top:845px;width:150px;text-align:center;font-weight:700;font-size:13.5px;line-height:1.25;color:#1a2a4a}
  .arrows{position:absolute;left:0;top:0}
  .footnote{position:absolute;left:347px;top:948px;width:500px;font-size:12.4px;line-height:1.3}
  .footnote p{text-align:justify;margin-bottom:8px}
  .footnote em{font-style:italic}
  .footer-grass{position:absolute;left:0;top:1033px;width:884px;height:111px;
    background:linear-gradient(180deg,rgba(255,255,255,0) 0%,#cdeb8f 40%,var(--grass-dark) 100%)}
</style>
</head>
<body>
<article class="flyer">
  <header class="header">
    <div class="header-illustration" role="img" aria-label="Dessin d'enfant : un arbre, un soleil souriant et une famille qui se tient la main avec un petit chien"></div>
    <div class="brand"><span class="brand-dot"></span><span class="brand-name">LA PRIMOVEL</span></div>
    <h1 class="title">
      <span class="title-line1">Les journées de la famille</span>
      <span class="title-line2">École Sainte-Ondine</span>
    </h1>
  </header>

  <section class="body">
    <p>L’école Sainte-Ondine souhaite ouvrir ses portes afin que vous puissiez partager avec votre enfant des moments de sa vie d’élève. Vous connaissez votre enfant sous plusieurs de ses facettes. Avec ce projet, vous pourrez maintenant le connaître en tant qu’élève œuvrant dans son milieu scolaire.</p>
    <p>Vous serez invités, à divers moments de l’année scolaire, à participer au quotidien de votre enfant, par exemple…</p>
    <ul class="checks">
      <li><svg width="14" height="14" viewBox="0 0 14 14"><circle cx="7" cy="7" r="6" fill="none" stroke="#3ea23a" stroke-width="1.3"/><path d="M4 7l2.2 2.2L10.5 4.5" fill="none" stroke="#3ea23a" stroke-width="1.5"/></svg><span>lors d’événements (ex.: la rentrée, chorale de Noël, fête foraine, etc.)</span></li>
      <li class="right"><svg width="14" height="14" viewBox="0 0 14 14"><circle cx="7" cy="7" r="6" fill="none" stroke="#3ea23a" stroke-width="1.3"/><path d="M4 7l2.2 2.2L10.5 4.5" fill="none" stroke="#3ea23a" stroke-width="1.5"/></svg><span>lors d’activités spéciales en classe (ex.: lecture, bricolage, présentation de métiers, etc.)</span></li>
      <li><svg width="14" height="14" viewBox="0 0 14 14"><circle cx="7" cy="7" r="6" fill="none" stroke="#3ea23a" stroke-width="1.3"/><path d="M4 7l2.2 2.2L10.5 4.5" fill="none" stroke="#3ea23a" stroke-width="1.5"/></svg><span>lors de sorties éducatives et sportives (ex.: patinage, bibliothèque, cinéma, etc.)</span></li>
    </ul>
    <p>De plus, vous aurez l’opportunité de venir passer une période dans la classe de votre enfant. Vous aurez ainsi le privilège de l’accompagner lors d’un moment d’apprentissage habituel.</p>
  </section>

  <svg class="arrows" width="884" height="1144" viewBox="0 0 884 1144" aria-hidden="true">
    <defs>
      <marker id="head" viewBox="0 0 10 10" refX="8" refY="5" markerWidth="7" markerHeight="7" orient="auto-start-reverse">
        <path d="M0 0L10 5L0 10" fill="none" stroke="#d8393a" stroke-width="1.8"/>
      </marker>
    </defs>
    <g stroke="#d8393a" stroke-width="2" fill="none">
      <line x1="374" y1="794" x2="318" y2="836" marker-start="url(#head)" marker-end="url(#head)"/>
      <line x1="473" y1="799" x2="532" y2="837" marker-start="url(#head)" marker-end="url(#head)"/>
      <line x1="332" y1="919" x2="521" y2="919" marker-start="url(#head)" marker-end="url(#head)"/>
    </g>
  </svg>

  <div class="note" style="left:279px;top:647px;width:288px;height:109px">
    <h3>POUR L’ENFANT :</h3>
    <ul>
      <li>Être fier de partager un moment de sa vie scolaire, en toute simplicité, avec son parent.</li>
      <li>Développer son plein potentiel.</li>
      <li>Favoriser sa réussite éducative.</li>
    </ul>
  </div>

  <div class="note" style="left:40px;top:781px;width:242px;height:90px">
    <h3>POUR L’ENFANT :</h3>
    <ul>
      <li>Vivre un projet rassembleur.</li>
      <li>Valoriser le travail de l’équipe- école.</li>
      <li>Rayonner dans sa communauté.</li>
    </ul>
  </div>

  <div class="note" style="left:40px;top:894px;width:242px;height:97px">
    <h3>POUR L’ENSEIGNANT :</h3>
    <ul>
      <li>Encourager la réussite de ses élèves.</li>
      <li>Multiplier les moments privilégiés parent-enfant-enseignant dans le milieu scolaire.</li>
    </ul>
  </div>

  <div class="note" style="left:596px;top:806px;width:247px;height:123px">
    <h3>POUR LE PARENT :</h3>
    <ul>
      <li>Développer un entiment d’appartenance envers l’école.</li>
      <li>Découvrir son enfant en tant qu’élève.</li>
      <li>Participer à la réussite et à la persévérance scolaire de son enfant.</li>
    </ul>
  </div>

  <div class="role" style="left:380px;top:747px">Enfant</div>
  <div class="role small" style="left:254px;top:833px">École<br>Enseignant(e)s</div>
  <div class="role" style="left:518px;top:835px">Parent</div>
  <div class="hub">Les journées de la famille de Sainte-Ondine</div>

  <div class="footnote">
    <p>Pour chaque occasion reliée au projet « Les journées de la famille de Sainte-Ondine»* vous serez informés par l’enseignant(e) de votre enfant afin que vous puissiez y participer.</p>
    <p>*Surveillez les apparitions du logo sur les communications lors des <em>Journées de la famille de Sainte-Ondine!</em></p>
  </div>

  <div class="footer-grass" role="img" aria-label="Herbe verte avec fleurs et papillons jaunes"></div>
</article>
</body>
</html>
```